Retail Photo Calendar of Anchorage, Alaska

I am a professional photographer in Anchorage, Alaska. I'm looking for a designer to create a unique, pleasing design for a 12-month (24 pages plus front and back cover) 2016 RETAIL calendar using images of mine of the Anchorage, Alaska area. This is not a promotional calendar. This calendar will be sold to the public in retail stores. So it's more about the calendar & photos than my name. Design must be appealing to the average consumer. The designer would be responsible for completing the entire calendar project to give plate-ready files. We’ll need both the raw InDesign files with links, as well as a PDF to be printed as a proof and submitted to the printer.

Specs for the calendar are:
• one vertical photo on front cover
• back cover
• inside back cover pages x 2
• Grid page for each month
• 12 horizontal photos for the monthly pages based on these specifications:
o Size: 8 7/8” x 12”
o Pages: Front and Back Cover plus 24 pages

Attached are two sample designs, one I like (file name “sample inside good”) and one I don’t like (sample inside bad). The one I like and what I’d want for my calendar is;
• more elegant design than the bad design
• small photo inserted on the grid page
• Unique fonts
• Nice ghosted back design element (sun in this case—which matches the month of July in Alaska)
• A quote

The one I don’t like (bad) is:
• Too much like a block
• Fonts are not very elegant
• Not much in the way of design going on here

I will supply:
• Excell document with approximately 100 dates for holiday’s, moon phases and special days.
• High resolution files of the 13 main images and 12 smaller insets
• Copy for each month including; captions for photos, quotes etc.
• The actual dates for a 2016 calendar

In order for me to choose a designer, what I’m expecting for this initial design is for the designer to offer the following;

1. A design for the cover, using the vertical image of the dog team supplied - and this copy: Anchorage, Alaska & Vicinity 2016 Calendar Photography by Dale Brannock

2. A design for ONE month on the inside--- ( 2 pages) photo placement, caption, calendar grid, design element, quote, small photo and previous/next month small grid. Do this using the one horizontal photo (airplanes) supplied – and greeking text for the potential copy of the photo caption, quote, etc.

A sample of what I'm looking for the designer to send me to choose their design is in the file labeled: "Cover and Inside Sample" --- the picture of an existing cover & inside of a calendar.

Once I choose the design and designer I prefer, he/she and I will then work together as I supply the rest of the images, dates and copy as mentioned above. Tweaks to be made as we go along. The deadline for the print-ready final, is to be completed by August 15, 2014 -- Once the final complete designs are made and confirmed to work for the printer is when I'll pay the designer the amount pledged.

PLEASE feel free to contact me before starting design work if I can help clarify what I am looking for here.

Target Market(s)

The general public living in or visiting Anchorage, Alaska

Industry/Entity Type

Printer

Font styles to use
Serif

Requirements
Must have
• elegant pleasing design

```html
<!DOCTYPE html>
<html lang="en">
<head>
<meta charset="utf-8">
<title>Anchorage, Alaska &amp; Vicinity 2016 Calendar – Cover Spread</title>
<link rel="stylesheet" href="https://fonts.googleapis.com/css2?family=Cinzel:wght@400;500&family=Cormorant+Garamond:wght@300;400&family=Great+Vibes&family=Open+Sans:wght@400&display=swap">
<style>
  :root {
    --paper: #ffffff;
    --band-blue: #1e2c7c;
    --band-blue-light: #27389a;
    --title-blue: #8eaeff;
    --ink-blue: #2b3fa6;
    --icon-blue: #4a7fe0;
    --silver-hi: #f4f4f4;
    --silver-lo: #8d8f96;
    --street-top: #6e5b47;
    --crowd: #3a3536;
    --snow: #e4e7ec;
    --snow-bright: #f3f4f6;
  }
  * { box-sizing: border-box; margin: 0; padding: 0; }
  html, body {
    width: 882px; height: 1200px; overflow: hidden; background: var(--paper);
  }
  .calendar-spread { position: relative; width: 882px; height: 1200px; background: var(--paper); }

  /* Back cover (printed upside down so it reads correctly when folded) */
  .back-cover { position: absolute; left: 0; top: 0; width: 882px; height: 600px; }
  .imprint {
    position: absolute; left: 0; right: 0; top: 224px;
    transform: rotate(180deg);
    text-align: center; color: var(--ink-blue);
  }
  .imprint-label {
    font-family: "Cinzel", serif; font-size: 10px; letter-spacing: 1px;
  }
  .imprint-signature {
    font-family: "Great Vibes", cursive; font-size: 30px; line-height: 34px;
  }
  .imprint-contact {
    font-family: "Open Sans", sans-serif; font-size: 9.5px; line-height: 11px; margin-top: 8px;
  }
  .imprint-social {
    display: flex; flex-direction: column; align-items: center; gap: 5px; margin-top: 9px;
    font-family: "Open Sans", sans-serif; font-size: 9.5px;
  }
  .imprint-social span { display: inline-flex; align-items: center; gap: 5px; }
  .social-dot { width: 12px; height: 12px; border-radius: 50%; background: var(--icon-blue); display: inline-block; }

  /* Front cover */
  .front-cover { position: absolute; left: 0; top: 600px; width: 882px; height: 600px; background: var(--paper); }
  .photo-strip {
    position: absolute; left: 0; top: 0; width: 62px; height: 600px;
    background: linear-gradient(180deg, #7a5e4c 0%, #c9ccd2 22%, #3b3a40 55%, #6f7fa0 75%, var(--snow) 100%);
  }
  .title-band {
    position: absolute; left: 65px; top: 0; width: 232px; height: 600px;
    background: linear-gradient(180deg, var(--band-blue-light) 0%, var(--band-blue) 100%);
    overflow: hidden;
  }
  .band-photo {
    position: absolute; left: 0; bottom: 0; width: 232px; height: 170px;
    background: linear-gradient(180deg, rgba(30,44,124,0) 0%, rgba(200,210,232,0.55) 45%, var(--snow) 100%);
  }
  .ghost-title {
    position: absolute; left: 0; right: 0; top: 462px;
    font-family: "Cormorant Garamond", serif; font-weight: 300;
    font-size: 40px; line-height: 27px; text-transform: uppercase;
    color: rgba(255,255,255,0.55); text-align: center; white-space: nowrap;
  }
  .ghost-title .small { font-size: 32px; }
  .cover-title {
    position: absolute; left: 0; right: 0; top: 78px; text-align: center;
    font-family: "Cinzel", serif; color: var(--title-blue);
    font-size: 27px; line-height: 25px;
  }
  .cover-title .amp {
    position: absolute; left: 0; right: 0; top: 44px;
    font-family: "Cormorant Garamond", serif; font-size: 44px;
    color: rgba(142,174,255,0.35);
  }
  .cover-title .line { position: relative; display: block; }
  .cover-year {
    position: absolute; left: 0; right: 0; top: 146px; text-align: center;
    font-family: "Cormorant Garamond", serif; font-weight: 400; font-size: 66px; line-height: 66px;
    background: linear-gradient(180deg, var(--silver-hi) 15%, var(--silver-lo) 60%, var(--silver-hi) 95%);
    -webkit-background-clip: text; background-clip: text; color: transparent;
  }
  .year-rule {
    position: absolute; left: 46px; width: 140px; top: 218px; height: 1px;
    background: rgba(142,174,255,0.6);
  }
  .cover-subtitle {
    position: absolute; left: 0; right: 0; top: 222px; text-align: center;
    font-family: "Cinzel", serif; font-size: 9.5px; letter-spacing: 1.6px; color: var(--title-blue);
  }
  .cover-credit {
    position: absolute; left: 0; right: 0; top: 260px; text-align: center; color: var(--title-blue);
    font-family: "Cinzel", serif; font-size: 10px; letter-spacing: 0.5px;
  }
  .cover-signature {
    position: absolute; left: 0; right: 0; top: 272px; text-align: center;
    font-family: "Great Vibes", cursive; font-size: 30px; color: #ffffff;
  }
  .hero-photo {
    position: absolute; left: 301px; top: 0; width: 581px; height: 600px;
    background: linear-gradient(180deg, var(--street-top) 0%, #5d6a5a 12%, #4a4442 22%, var(--crowd) 38%, #8a8e97 52%, var(--snow) 66%, var(--snow-bright) 88%, #c9ccd1 100%);
    overflow: hidden;
  }
  .ghost-year {
    position: absolute; left: 22px; bottom: -52px;
    font-family: "Cormorant Garamond", serif; font-weight: 300; font-size: 262px; line-height: 262px;
    letter-spacing: 6px; color: rgba(255,255,255,0.45);
  }
</style>
</head>
<body>
<main class="calendar-spread">
  <section class="back-cover">
    <div class="imprint">
      <p class="imprint-label">PHOTOGRAPHY BY</p>
      <p class="imprint-signature">Dale Brannock</p>
      <p class="imprint-contact">Harbor Light Avenue<br>Anchorage, AK 99501<br>907-555-0142<br>dalebrannockphoto@mailbox.com</p>
      <div class="imprint-social">
        <span><i class="social-dot"></i>Dale Brannock</span>
        <span><i class="social-dot"></i>@Dale Brannock</span>
      </div>
    </div>
  </section>

  <section class="front-cover">
    <div class="photo-strip" role="img" aria-label="Narrow slice of the dog-sled race photo: downtown storefronts and crowd"></div>

    <div class="title-band">
      <div class="band-photo" role="img" aria-label="Faded slice of the dog team running on the snowy street"></div>
      <p class="ghost-title">Anchora<br>Alaska<br><span class="small">&amp; Vicinity</span></p>

      <h1 class="cover-title">
        <span class="line">ANCHORAGE,</span>
        <span class="line">ALASKA</span>
        <span class="amp">&amp;</span>
        <span class="line">VICINITY</span>
      </h1>
      <p class="cover-year">2016</p>
      <div class="year-rule"></div>
      <p class="cover-subtitle">12 MONTH CALENDAR</p>
      <p class="cover-credit">PHOTOGRAPHY BY</p>
      <p class="cover-signature">Dale Brannock</p>
    </div>

    <div class="hero-photo" role="img" aria-label="Vertical photo of a sled dog team racing down a snowy downtown Anchorage street lined with crowds and flags">
      <span class="ghost-year">2016</span>
    </div>
  </section>
</main>
</body>
</html>
```